Veltrano Energy Business Card Design

website: www.veltranoenergy.example
Project: Business Card Design for Veltrano Energy
Name: Dorian Kettle
Title: Founder / Operations Strategist
Visual Identity & Logo:
Logo File: VEL-Logo-FullGradient-Final.png (Attached).
Color Palette: The brand relies on a distinctive Cyan (Blue) to Lime Green gradient.
Background Preference: We want a Dark Mode aesthetic (Deep Matte Black, Charcoal, or Dark Slate) to make the neon gradient of the logo pop. This feels more "tech/industrial" than a standard white card.
Design Aesthetic (The "Ops" Vibe):
Concept: "Grid & Infrastructure." We are a solar rental company, focusing on logistics and access.
Typography: White, bold sans-serif text for contact info. High contrast against the dark background.
Accents: Use the Cyan or Lime Green from the logo for thin divider lines or edge painting.
Avoid: No orange/gold (clashes with logo). No cartoon leaves.
Layout Requirements:
Front: Large, centered logo. Maybe a subtle UV gloss spot varnish over the logo icon.
Back: Name, Title, Contact Info.
Texture: Matte finish cardstock with gloss elements.
sample mock up of information on card: https://brivomarkco-my.filehost.example/:i:/g/personal/dorian_kettle_veltranoenergy_example/AbCdEfGhIjKlMnOpQrStUvWxYz012345678?e=Xy12Ab
Logo: https://brivomarkco.filehost.example/:i:/s/VeltranoEnergy/ZyXwVuTsRqPoNmLkJiHgFeDcBa9876543210?e=Pq34Cd

```html
<!DOCTYPE html>
<html lang="en">
<head>
<meta charset="utf-8">
<title>Veltrano Energy Business Card</title>
<link href="https://fonts.googleapis.com/css2?family=Poppins:wght@400;600;800&family=Roboto:wght@400&display=swap" rel="stylesheet">
<style>
:root{
  --page:#dcdcdc;
  --card:#050505;
  --charcoal:#3a3a3a;
  --cyan:#08a9d6;
  --aqua:#16d3d3;
  --lime:#9fe03a;
  --white:#ffffff;
  --grad:linear-gradient(90deg,var(--cyan),var(--aqua) 45%,var(--lime));
}
*{margin:0;padding:0;box-sizing:border-box}
html,body{width:933px;height:1200px;overflow:hidden;background:var(--page)}
body{position:relative;font-family:'Poppins',sans-serif;color:var(--white)}
.card{position:absolute;left:85px;width:763px;height:435px;overflow:hidden;
  background:radial-gradient(ellipse 420px 300px at 0 0,var(--charcoal),var(--card) 75%);
  box-shadow:14px 22px 28px rgba(0,0,0,.35)}
.card--front{top:127px}
.card--back{top:638px}
.texture-band{position:absolute;left:0;bottom:0;width:100%;height:28px;
  background:linear-gradient(90deg,rgba(255,255,255,.12),rgba(255,255,255,.03) 70%,transparent)}
.brand{position:absolute;display:flex;align-items:center;gap:14px}
.brand__mark{background:var(--cyan)}
.brand__name{font-weight:400;color:var(--aqua);line-height:1;white-space:nowrap}
.tagline{position:absolute;font-family:'Roboto',sans-serif;color:var(--white);white-space:nowrap}
/* front */
.card--front .brand{left:0;right:0;top:76px;justify-content:center}
.card--front .brand__mark{width:58px;height:58px}
.card--front .brand__name{font-size:54px}
.card--front .tagline{left:0;right:0;top:210px;text-align:center;font-size:13.5px}
.pills{position:absolute;left:126px;top:268px;width:510px;height:37px;border-radius:19px;
  background:var(--grad);display:flex;overflow:hidden}
.pills span{flex:auto;display:flex;align-items:center;justify-content:center;
  font-weight:800;font-size:15px;color:#07121a;border-right:1.5px solid var(--card)}
.pills span:last-child{border-right:0}
.site-front{position:absolute;left:0;right:0;top:318px;text-align:center;font-size:22px;
  letter-spacing:9px;background:var(--grad);-webkit-background-clip:text;background-clip:text;color:transparent}
.site-front b{font-weight:800}
/* back */
.card--back .brand{left:63px;top:44px}
.card--back .brand__mark{width:38px;height:38px}
.card--back .brand__name{font-size:38px}
.card--back .tagline{left:136px;top:124px;font-size:8.5px}
.person{position:absolute;left:67px;top:177px}
.person__name{font-size:40px;font-weight:400;line-height:1.2;white-space:nowrap;background:var(--grad);
  -webkit-background-clip:text;background-clip:text;color:transparent}
.person__name b{font-weight:800}
.person__role{margin-top:4px;font-size:17.5px;line-height:22px}
.promise{position:absolute;left:67px;top:298px;font-weight:800;font-size:17px;line-height:24.5px;
  background:linear-gradient(90deg,var(--cyan),var(--lime));-webkit-background-clip:text;background-clip:text;color:transparent}
.contact-rail{position:absolute;left:389px;top:175px;width:22px;height:140px;border-radius:11px;
  background:linear-gradient(180deg,var(--lime),var(--aqua) 60%,#07d6f0)}
.contact-rail svg{position:absolute;left:5px;width:12px;height:12px}
.contacts{position:absolute;left:432px;font-size:17.5px;line-height:22px;white-space:nowrap}
.contacts--web{font-size:16px}
.offices{position:absolute;left:432px;top:328px;display:flex;align-items:center;gap:10px}
.offices__label{font-weight:800;font-size:17px;margin-right:4px;background:linear-gradient(90deg,var(--cyan),var(--lime));
  -webkit-background-clip:text;background-clip:text;color:transparent}
.office-dot{width:38px;height:38px;border-radius:50%;border:2px solid #eee}
.office-dot--us{background:linear-gradient(180deg,#3c3b6e 0 45%,#e4e4e4 45% 60%,#b22234 60%)}
.office-dot--ca{background:linear-gradient(90deg,#d52b1e 0 28%,#fff 28% 72%,#d52b1e 72%)}
.office-dot--uk{background:linear-gradient(135deg,#012169 0 40%,#c8102e 40% 60%,#012169 60%)}
.frame-lines{position:absolute;left:0;top:0}
</style>
</head>
<body>

<section class="card card--front">
  <div class="brand">
    <span class="brand__mark"></span>
    <span class="brand__name">Veltrano Energy</span>
  </div>
  <p class="tagline">RENT SOLAR. GERNERATE POWER.SAVE SMARTER</p>
  <div class="pills">
    <span>NO DEBT</span><span>NO LIENS</span><span>NO MAINTENANCE</span><span>JUST SAVINGS</span>
  </div>
  <p class="site-front">www.<b>veltranoenergy</b>.example</p>
  <div class="texture-band" role="img" aria-label="Faint chevron grid texture"></div>
</section>

<section class="card card--back">
  <div class="brand">
    <span class="brand__mark"></span>
    <span class="brand__name">Veltrano Energy</span>
  </div>
  <p class="tagline">RENT SOLAR. GERNERATE POWER.SAVE SMARTER</p>

  <div class="person">
    <h1 class="person__name"><b>Dorian</b> Kettle</h1>
    <p class="person__role">Founder/Operations<br>Strategist</p>
  </div>
  <p class="promise">No debt, No liens,<br>No maintenance,<br>Just savings.</p>

  <svg class="frame-lines" width="763" height="435" viewBox="0 0 763 435" aria-hidden="true">
    <g fill="none" stroke-width="1.2">
      <line x1="690" y1="0" x2="690" y2="376" stroke="#9fe03a"/>
      <line x1="695" y1="0" x2="695" y2="376" stroke="#5ed98a"/>
      <line x1="702" y1="0" x2="702" y2="376" stroke="#16d3d3"/>
      <polyline points="401,328 401,376 702,376" stroke="#16d3d3"/>
    </g>
    <circle cx="401" cy="328" r="3.5" fill="#9fe03a"/>
  </svg>

  <div class="contact-rail">
    <svg style="top:10px" viewBox="0 0 24 24" aria-label="Phone"><path d="M6 2l4 4-2 3a12 12 0 0 0 7 7l3-2 4 4-3 4C10 22 2 14 2 5z" fill="#07121a"/></svg>
    <svg style="top:62px" viewBox="0 0 24 24" aria-label="Location"><path d="M12 2a7 7 0 0 0-7 7c0 5 7 11 7 11s7-6 7-11a7 7 0 0 0-7-7zm0 10a3 3 0 1 1 0-6 3 3 0 0 1 0 6z" fill="#07121a"/></svg>
    <svg style="top:118px" viewBox="0 0 24 24" aria-label="Website"><g fill="none" stroke="#07121a" stroke-width="2.2"><circle cx="12" cy="12" r="9"/><path d="M3 12h18M12 3c4 4 4 14 0 18M12 3c-4 4-4 14 0 18"/></g></svg>
  </div>

  <p class="contacts" style="top:179px">555.014.2297</p>
  <p class="contacts" style="top:219px">4120 Harbor Quarry Road<br>Lakeview, FL 30918</p>
  <p class="contacts contacts--web" style="top:282px">www.veltranoenergy.example</p>

  <div class="offices">
    <span class="offices__label">Offices</span>
    <span class="office-dot office-dot--us" role="img" aria-label="United States flag"></span>
    <span class="office-dot office-dot--ca" role="img" aria-label="Canada flag"></span>
    <span class="office-dot office-dot--uk" role="img" aria-label="United Kingdom flag"></span>
  </div>

  <div class="texture-band" role="img" aria-label="Faint chevron grid texture"></div>
</section>

</body>
</html>
```